Low Meadow Guild - Lanterns In Frost Artwork

I'm looking for artwork for our latest single "Lanterns in Frost". I'm looking for hi-res jpg files for use on our website, friendwall, tunedrift and echoharbour sites.
Check out our previous work for reference:
www.lowmeadowguild.example
https://www.vidstreamo.example/channel/QX7k--plorvZnmAAs-TdW4h
https://www.friendwall.example/lowmeadowguild/
https://tunedrift.example/low-meadow-guild

Target Market(s)

Indie music (e.g. Tinkers / Balm Fans)

Industry/Entity Type

Music Download

Requirements
Must have
• - the Low Meadow Guild logo
• - the song title Lanterns In Frost
Should not have
• - no direct Christmas imagery

```html
<!DOCTYPE html>
<html lang="en">
<head>
<meta charset="utf-8">
<title>Low Meadow Guild – Lanterns In Frost</title>
<link rel="stylesheet" href="https://fonts.googleapis.com/css2?family=Montserrat:wght@500;800&display=swap">
<style>
  :root {
    --backdrop: #d3cbb3;
    --cover-dark: #2a292c;
    --cover-grey: #8d8c8f;
    --cover-light: #c9c8ca;
    --ember: #c4582c;
    --ember-deep: #7a2c18;
    --title-red: #c21f1b;
    --logo-box: #1e1d1f;
    --logo-text: #e9e7e3;
  }
  * { margin: 0; padding: 0; box-sizing: border-box; }
  html, body {
    width: 1200px;
    height: 900px;
    overflow: hidden;
    background: var(--backdrop);
  }
  .cover {
    position: absolute;
    left: 200px;
    top: 50px;
    width: 800px;
    height: 800px;
    overflow: hidden;
    box-shadow: 0 10px 30px rgba(0, 0, 0, 0.2);
  }
  .cover-art {
    position: absolute;
    inset: 0;
    background:
      radial-gradient(ellipse at 28% 22%, rgba(230, 229, 231, 0.75), transparent 55%),
      linear-gradient(100deg, transparent 48%, rgba(196, 88, 44, 0.85) 62%, rgba(122, 44, 24, 0.9) 82%, rgba(196, 88, 44, 0.8) 100%),
      linear-gradient(180deg, var(--cover-dark) 0%, var(--cover-grey) 45%, var(--cover-dark) 100%);
  }
  .guild-logo {
    position: absolute;
    left: 80px;
    top: 80px;
    width: 92px;
    height: 92px;
    background: var(--logo-box);
    display: flex;
    align-items: center;
    justify-content: center;
    text-align: center;
    color: var(--logo-text);
    font-family: "Montserrat", sans-serif;
    font-weight: 500;
    font-size: 13px;
    line-height: 1.2;
    letter-spacing: 1px;
    text-transform: uppercase;
  }
  .single-title {
    position: absolute;
    left: 0;
    top: 300px;
    width: 100%;
    font-family: "Montserrat", sans-serif;
    font-weight: 800;
    font-size: 78px;
    line-height: 1.1;
    letter-spacing: 5px;
    color: var(--title-red);
    text-transform: uppercase;
    white-space: nowrap;
    transform: rotate(-7deg);
    transform-origin: 50% 50%;
  }
  .single-title span { display: block; }
  .single-title .line-one { padding-left: 250px; }
  .single-title .line-two { padding-left: 170px; }
</style>
</head>
<body>
  <main class="cover">
    <div class="cover-art" role="img" aria-label="Abstract textured photograph in frosty greys with warm orange light streaks"></div>
    <div class="guild-logo">Low<br>Meadow<br>Guild</div>
    <h1 class="single-title">
      <span class="line-one">Lanterns</span>
      <span class="line-two">In Frost</span>
    </h1>
  </main>
</body>
</html>
```